Baby Shower Invitation for Vectored Image Provided

Caroline & Desmond's Baby Shower - Black/White/Gold Colors preferred
Please use the vectored portrait image attached. I'd like us on the lower right side of the invitation.
Can be horizontal or vertical layout.
The second image attached has the information needed for you to complete.
I don't want that style copied, it is just an example.

```html
<!DOCTYPE html>
<html lang="en">
<head>
<meta charset="utf-8">
<title>Caroline Whitmore Baby Shower Invitation</title>
<link rel="stylesheet" href="https://fonts.googleapis.com/css2?family=Great+Vibes&family=Questrial&display=swap">
<style>
  :root {
    --cream: #f3efe5;
    --gold: #c9a862;
    --gold-soft: #e2cf8f;
    --ink: #141414;
    --white: #ffffff;
    --portrait-dark: #1f2326;
    --portrait-warm: #8a6a55;
  }
  html, body {
    margin: 0;
    padding: 0;
    overflow: hidden;
  }
  body {
    width: 846px;
    height: 1200px;
  }
  .invitation {
    position: relative;
    width: 846px;
    height: 1200px;
    overflow: hidden;
    background: var(--cream);
  }
  .backdrop-pattern {
    position: absolute;
    inset: 0;
    background:
      radial-gradient(ellipse at 15% 10%, rgba(226, 207, 143, 0.55), transparent 45%),
      radial-gradient(ellipse at 88% 15%, rgba(226, 207, 143, 0.5), transparent 40%),
      radial-gradient(ellipse at 8% 80%, rgba(226, 207, 143, 0.5), transparent 40%),
      radial-gradient(ellipse at 92% 85%, rgba(226, 207, 143, 0.5), transparent 40%),
      var(--cream);
  }
  .card-oval {
    position: absolute;
    left: 60px;
    top: 58px;
    width: 726px;
    height: 1065px;
    border-radius: 50%;
    background: var(--white);
    box-shadow: 2px 4px 10px rgba(0, 0, 0, 0.25);
    overflow: hidden;
  }
  .portrait-area {
    position: absolute;
    left: 245px;
    top: 760px;
    width: 237px;
    height: 320px;
    background: linear-gradient(180deg, var(--portrait-warm) 0%, var(--portrait-dark) 35%, var(--portrait-dark) 100%);
    border-radius: 40px 40px 0 0;
  }
  .line {
    position: absolute;
    left: 0;
    width: 846px;
    margin: 0;
    text-align: center;
    white-space: nowrap;
    transform: translateY(-50%);
  }
  .script {
    font-family: "Great Vibes", cursive;
    color: var(--gold);
    font-weight: 400;
  }
  .sans {
    font-family: "Questrial", sans-serif;
    color: var(--ink);
    letter-spacing: 0.5px;
  }
  .headline { top: 205px; font-size: 96px; }
  .tagline { top: 292px; font-size: 38px; }
  .intro-1 { top: 358px; font-size: 24px; }
  .intro-2 { top: 394px; font-size: 24px; }
  .honoree { top: 478px; font-size: 84px; left: 10px; }
  .date { top: 558px; font-size: 25px; }
  .venue { top: 628px; font-size: 50px; }
  .address { top: 668px; font-size: 24px; }
  .rsvp { top: 733px; font-size: 20px; }
  .registry { top: 772px; font-size: 32px; }
  sup { font-size: 0.55em; vertical-align: 0.7em; line-height: 0; }
</style>
</head>
<body>
  <main class="invitation">
    <div class="backdrop-pattern" role="img" aria-label="Gold glitter polka dot pattern on cream background"></div>
    <section class="card-oval">
      <div class="portrait-area" role="img" aria-label="Illustrated portrait of the expecting couple"></div>
    </section>

    <h1 class="line script headline">Oh Boy!</h1>
    <p class="line script tagline">A Little Man Is On The Way!</p>
    <p class="line sans intro-1">Please join us for a</p>
    <p class="line sans intro-2">Baby Shower honoring</p>
    <h2 class="line script honoree">Caroline Whitmore</h2>
    <p class="line sans date">Saturday 1<sup>st</sup> September, 11:30am-2:30pm</p>
    <p class="line script venue">The Fernhollow</p>
    <p class="line sans address">1487 Alder Ln. Raleigh, NC</p>
    <p class="line sans rsvp">RSVP to Desmond at 919-555-0142 by August 20<sup>th</sup></p>
    <p class="line script registry">Caroline is registered at Little Nest Baby</p>
  </main>
</body>
</html>
```